Dance Music Album cover

We need an album cover for the release of our artist Velvetmoonz

for Velvetmoonz for his 4 tracks.

The following mentions are required for Velvetmoonz's cover :

- Velvetmoonz

- Sky on fire

- TRK47 (not mandatory)

• benny kostrin feel, Pale Orbit Records feel, Ka Ru feel to it.

```html
<!DOCTYPE html>
<html lang="en">
<head>
<meta charset="utf-8">
<title>Velvetmoonz – Sky on fire</title>
<link rel="stylesheet" href="https://fonts.googleapis.com/css2?family=Londrina+Sketch&family=Londrina+Solid:wght@400&family=Indie+Flower&display=swap">
<style>
  :root {
    --bg: #e9e7e3;
    --frame: #ffffff;
    --ink-shadow: #2b2236;
    --acid-green: #2fe05a;
    --hot-orange: #f26a12;
    --magenta: #c42fe8;
    --violet: #6a45e6;
    --royal-blue: #1f2fd6;
    --aqua: #2ee8e0;
    --lime: #9bf02a;
    --scarlet: #e8262e;
    --title: #ffffff;
  }
  * { box-sizing: border-box; margin: 0; padding: 0; }
  html, body {
    width: 1200px;
    height: 900px;
    overflow: hidden;
    background: var(--bg);
  }
  .canvas {
    position: relative;
    width: 1200px;
    height: 900px;
  }
  .album-cover {
    position: absolute;
    left: 240px;
    top: 90px;
    width: 720px;
    height: 720px;
    background: var(--frame);
    padding: 10px;
    box-shadow: 0 6px 24px rgba(0,0,0,0.18);
  }
  .artwork-grid {
    position: relative;
    width: 100%;
    height: 100%;
    display: grid;
    grid-template-columns: 1fr 1fr;
    grid-template-rows: 1fr 1fr;
    gap: 8px;
  }
  .artwork-panel { width: 100%; height: 100%; }
  .panel-green-orange {
    background:
      radial-gradient(circle at 45% 45%, var(--hot-orange) 0 28%, transparent 55%),
      radial-gradient(circle at 85% 80%, var(--magenta) 0 18%, transparent 40%),
      linear-gradient(160deg, var(--acid-green), #5ff07a 60%, var(--magenta));
  }
  .panel-violet-orange {
    background:
      radial-gradient(circle at 40% 45%, var(--hot-orange) 0 25%, transparent 52%),
      radial-gradient(circle at 85% 75%, #f0a040 0 15%, transparent 38%),
      linear-gradient(200deg, var(--royal-blue), var(--violet) 55%, #8f6ff0);
  }
  .panel-orange-aqua {
    background:
      radial-gradient(circle at 40% 60%, var(--aqua) 0 26%, transparent 54%),
      radial-gradient(circle at 85% 75%, #6af0ff 0 16%, transparent 38%),
      linear-gradient(170deg, var(--hot-orange), #ff7a20 55%, var(--aqua));
  }
  .panel-lime-blue {
    background:
      radial-gradient(circle at 40% 50%, var(--scarlet) 0 20%, transparent 46%),
      radial-gradient(circle at 45% 75%, var(--royal-blue) 0 22%, transparent 48%),
      linear-gradient(190deg, var(--lime), var(--acid-green) 50%, var(--royal-blue));
  }
  .cover-title {
    position: absolute;
    left: 0;
    right: 0;
    top: 40%;
    text-align: center;
    pointer-events: none;
  }
  .artist-name {
    display: block;
    font-family: "Londrina Solid", "Londrina Sketch", cursive;
    font-size: 112px;
    line-height: 1;
    letter-spacing: 2px;
    text-transform: uppercase;
    color: var(--title);
    text-shadow:
      2px 2px 0 var(--ink-shadow),
      -2px 2px 0 var(--ink-shadow),
      2px -2px 0 var(--ink-shadow),
      -2px -2px 0 var(--ink-shadow),
      4px 6px 8px rgba(0,0,0,0.45);
  }
  .release-title {
    display: block;
    margin-top: -4px;
    padding-right: 36px;
    text-align: right;
    font-family: "Indie Flower", cursive;
    font-size: 60px;
    line-height: 1;
    color: var(--title);
    text-shadow:
      2px 2px 0 var(--ink-shadow),
      -2px 2px 0 var(--ink-shadow),
      2px -2px 0 var(--ink-shadow),
      -2px -2px 0 var(--ink-shadow),
      3px 5px 6px rgba(0,0,0,0.4);
  }
</style>
</head>
<body>
  <main class="canvas">
    <section class="album-cover">
      <div class="artwork-grid">
        <div class="artwork-panel panel-green-orange" role="img" aria-label="Pop-art tinted photo of vintage toy robots in green, orange and magenta"></div>
        <div class="artwork-panel panel-violet-orange" role="img" aria-label="Pop-art tinted photo of vintage toy robots in violet, blue and orange"></div>
        <div class="artwork-panel panel-orange-aqua" role="img" aria-label="Pop-art tinted photo of vintage toy robots in orange and aqua"></div>
        <div class="artwork-panel panel-lime-blue" role="img" aria-label="Pop-art tinted photo of vintage toy robots in lime green, blue and red"></div>
      </div>
      <h1 class="cover-title">
        <span class="artist-name">Velvetmoonz</span>
        <span class="release-title">Sky on fire</span>
      </h1>
    </section>
  </main>
</body>
</html>
```